KVO - Redesign (PSD Files Only)

Requirements for the site:

1. We need our logo recreated, please use the same design and change colors to work on a white background

2. The site is a "Wizard" based site, that takes the customer through the process of creating a unique web presence that suits there needs

3.Colors Needed - Main "Dark Blue" Secondary = "Dark Grey" -Other = "Light Grey and White"

4.We need a CRISP CLEAN DESIGN, simple design

5.Wireframes are a general layout and may be modified by you to enhance the design

6. We want a complete web 5.0 look with big buttons and text boxes

7.The more personality the better

8. Current Site brightmorrowco.example

9.See attachments for wireframes

10. Designer should deliver PSD files, no coding is required

11. The portfolio wireframe, should look like the design of the pixelharbor portfolio template
Updates

KEEP IT SIMPLE.,.....

We like the quillframe scaffold style of designs

```html
<!DOCTYPE html>
<html lang="en">
<head>
<meta charset="utf-8">
<title>KVO – Custom Website Design</title>
<link href="https://fonts.googleapis.com/css2?family=PT+Sans:wght@400;700&family=PT+Sans+Narrow:wght@400;700&family=Roboto:wght@300;400&display=swap" rel="stylesheet">
<style>
:root{
  --blue:#1d3f9e;
  --blue-dark:#14307f;
  --blue-text:#1f4aa6;
  --grey-dark:#333;
  --grey:#666;
  --grey-light:#999;
  --line:#dcdcdc;
  --panel:#f4f4f4;
  --green:#6eae14;
  --orange:#f7a400;
  --white:#fff;
}
*{margin:0;padding:0;box-sizing:border-box}
html,body{width:1031px;height:1200px;overflow:hidden;background:var(--white)}
body{position:relative;font-family:"Roboto",sans-serif;color:var(--grey)}
.abs{position:absolute}

/* nav */
.topbar{left:0;top:0;width:1031px;height:46px;background:linear-gradient(#2551b8,var(--blue-dark));}
.nav{display:flex;height:46px;margin-left:70px;list-style:none}
.nav li{font-family:"PT Sans Narrow",sans-serif;font-size:16px;color:var(--white);padding:0 18px;line-height:46px;border-right:1px solid rgba(255,255,255,.15)}
.nav li:last-child{border:none}
.social{left:705px;top:11px;display:flex;gap:6px}
.social span{width:24px;height:24px;border-radius:50%;background:var(--white)}
.phone{left:847px;top:11px;font-family:"PT Sans",sans-serif;font-size:19px;color:var(--white)}

/* hero */
.hero{left:0;top:46px;width:1031px;height:452px;background:linear-gradient(#fff 70%,#f1f1f1)}
.headline{left:0;top:80px;width:1031px;text-align:center;font-family:"PT Sans",sans-serif;font-size:34px;color:var(--blue-text)}
.subhead{left:0;top:126px;width:1031px;text-align:center;font-family:"PT Sans",sans-serif;font-size:20px;color:var(--grey-dark)}
.tagline{left:0;top:155px;width:1031px;text-align:center;font-size:12.5px;font-weight:300;color:var(--grey)}
.bubble{border-radius:50%;display:flex;align-items:center;justify-content:center;text-align:center;color:var(--white);font-family:"PT Sans Narrow",sans-serif;line-height:1.05}
.bubble.support{left:78px;top:195px;width:134px;height:134px;background:radial-gradient(circle at 40% 30%,#8fd12a,var(--green) 60%,#4f8a0a);font-size:18px}
.bubble.support b{font-weight:400;font-size:23px}
.bubble.money{left:850px;top:191px;width:112px;height:112px;background:radial-gradient(circle at 40% 30%,#2f5fcc,var(--blue-dark) 70%);font-size:16.5px}
.bubble.save{left:787px;top:303px;width:112px;height:112px;background:radial-gradient(circle at 40% 30%,#ffd233,var(--orange) 70%);font-size:16.5px}
.brand{left:440px;top:200px;width:180px;text-align:center}
.brand .mark{width:70px;height:70px;margin:0 auto;border:8px solid var(--blue);border-radius:6px}
.brand .name{font-family:"PT Sans Narrow",sans-serif;font-size:26px;color:var(--blue);margin-top:6px}
.brand .short{font-family:"PT Sans Narrow",sans-serif;font-size:24px;color:var(--blue);position:absolute;left:0;right:0;top:20px}
.quote-note{left:44px;top:362px;width:200px;text-align:center;font-family:"PT Sans",sans-serif;font-size:13.5px;color:var(--grey-dark)}
.quote-note strong{display:block;font-weight:400;font-size:19px}
.step-label{left:455px;top:357px;width:153px;text-align:center;font-family:"PT Sans",sans-serif;font-size:13px;color:var(--grey-dark)}
.progress{left:455px;top:378px;width:153px;height:17px;border:1px solid #bbb;border-radius:3px;background:var(--white);overflow:hidden}
.progress i{display:block;width:47px;height:100%;background:linear-gradient(#ffce2c,var(--orange))}
.project-input{left:318px;top:412px;width:305px;height:29px;border:1px solid #ccc;border-radius:3px;background:var(--white);font-size:12px;color:var(--grey-light);padding:7px 11px;font-weight:300}
.start-btn{left:629px;top:411px;width:138px;height:31px;border-radius:4px;background:linear-gradient(#555,#222);color:var(--white);font-family:"PT Sans",sans-serif;font-size:14px;text-align:center;line-height:31px}

/* service cards */
.card{top:533px;width:224px;height:281px;border:1px solid var(--line);border-radius:3px;background:linear-gradient(#fff 55%,#efefef);padding:20px 18px 0 19px}
.card h2{font-family:"PT Sans",sans-serif;font-weight:400;font-size:20px;color:var(--blue-text);margin-bottom:6px}
.card p{font-size:11.5px;font-weight:300;line-height:18px;color:var(--grey);margin-bottom:3px}
.card ul{list-style:none;margin-left:5px}
.card li{font-size:12.5px;font-weight:300;color:var(--grey-dark);line-height:15.5px;padding:4px 0 4px 11px;position:relative}
.card li::before{content:"›";position:absolute;left:0;top:3px;font-size:14px;color:var(--grey-dark)}

/* portfolio */
.showcase{left:54px;top:861px;width:922px;height:192px;border:1px solid #e4e4e4;border-radius:3px;background:var(--white);box-shadow:0 6px 8px -6px rgba(0,0,0,.15)}
.thumb{top:886px;width:269px;height:138px;border:1px solid #ddd;padding:5px;background:var(--white);box-shadow:0 1px 3px rgba(0,0,0,.15)}
.thumb div{width:100%;height:100%}
.arrow{top:926px;width:30px;height:60px;background:#eaeaea;display:flex;align-items:center;justify-content:center}
.arrow.left{left:54px;border-radius:0 30px 30px 0}
.arrow.right{left:946px;border-radius:30px 0 0 30px}

/* footer */
.footer{left:0;top:1096px;width:1031px;height:104px;border-top:3px solid #f3f3f3}
.footer-links{left:59px;top:1131px;font-family:"PT Sans",sans-serif;font-size:13.5px;color:var(--grey-dark)}
.footer-links span{color:#999;margin:0 5px}
.copyright{left:58px;top:1158px;font-size:11.5px;font-weight:300;color:var(--grey-dark)}
.partner-badge{left:810px;top:1125px;width:148px;height:52px;border:1px solid #ddd;background:var(--white);box-shadow:0 1px 3px rgba(0,0,0,.12)}
.partner-badge i{position:absolute;left:1px;top:1px;width:50px;height:48px;background:#3d6ad8}
</style>
</head>
<body>

<header class="topbar abs">
  <ul class="nav">
    <li>HOME</li><li>ABOUT</li><li>PORTFOLIO</li><li>CONTACT US</li>
  </ul>
</header>
<div class="social abs" aria-label="Social links"><span></span><span></span><span></span><span></span></div>
<div class="phone abs">1.800.555.0142</div>

<section class="hero abs"></section>
<h1 class="headline abs">Get a Custom Website Design in 21 Days or LESS!</h1>
<p class="subhead abs">Find our why we're the #1 custom website design marketplace.</p>
<p class="tagline abs">Our Network of designers will create 50+ web design samples for you to choose and our marketing experts will pave the way for your success</p>

<svg class="abs" style="left:0;top:0" width="1031" height="460" aria-hidden="true">
  <g fill="none" stroke="#d6d6d6" stroke-width="1.3">
    <path d="M440 305 C380 320 350 230 232 245"/>
    <path d="M232 245 l10 -10 M232 245 l12 5"/>
    <path d="M318 410 C290 400 280 360 225 373"/>
    <path d="M225 373 l10 -9 M225 373 l11 5"/>
    <path d="M600 275 C680 290 700 180 830 215"/>
    <path d="M830 215 l-9 -9 M830 215 l-12 3"/>
    <path d="M605 300 C680 265 760 270 815 285"/>
    <path d="M815 285 l-9 -8 M815 285 l-3 -11"/>
    <path d="M800 405 C815 410 810 415 800 418"/>
  </g>
</svg>

<div class="bubble support abs"><div>24/7 Customer<br><b>Support</b></div></div>
<div class="bubble money abs"><div>100%<br>Moneyback<br>Gaurantee</div></div>
<div class="bubble save abs"><div>Save1000's on<br>Web Design</div></div>

<div class="brand abs">
  <div class="mark"></div>
  <div class="short">KVO</div>
  <div class="name">Brightmorrow Co</div>
</div>

<div class="quote-note abs">100% No Obligation<strong>FREE WEB QUOTE</strong></div>
<div class="step-label abs">Step: 1</div>
<div class="progress abs"><i></i></div>
<div class="project-input abs">Name your project</div>
<div class="start-btn abs">Start Your Project</div>

<article class="card abs" style="left:53px">
  <h2>Why Choose KVO?</h2>
  <p>We are a full service design &amp; maketing company that will handle everthing.</p>
  <ul><li>Dedicated Project Manager</li><li>Single Point of Contact</li><li>Marketing Coaches</li><li>Low Cost</li><li>50+ Design Samples you to choose</li></ul>
</article>
<article class="card abs" style="left:285px">
  <h2>Web Services</h2>
  <p>We Specialize in the following design services</p>
  <ul><li>Web Design</li><li>Ecommerce Design</li><li>Web Programming</li><li>Logo Design</li><li>Stationary/Print Design</li><li>Ad Design</li><li>Email Template Design</li></ul>
</article>
<article class="card abs" style="left:519px">
  <h2>Marketing Services</h2>
  <p>We Handle all online marketing includ-ing the following</p>
  <ul><li>Search Ads</li><li>Local Map Marketing</li><li>Search Engine Optimization</li><li>Email Marketing</li><li>Social Media Marketing</li></ul>
</article>
<article class="card abs" style="left:751px">
  <h2>Maintainence Services</h2>
  <p>Let us maintain your site and save up to 50% on the followings</p>
  <ul><li>Website Hosting</li><li>Software Upgrade</li><li>Custom Web Programming</li><li>Website Marketing</li></ul>
</article>

<section class="showcase abs"></section>
<div class="arrow left abs"><svg width="12" height="22"><path d="M10 2 L2 11 L10 20" fill="none" stroke="#999" stroke-width="1.5"/></svg></div>
<div class="arrow right abs"><svg width="12" height="22"><path d="M2 2 L10 11 L2 20" fill="none" stroke="#999" stroke-width="1.5"/></svg></div>
<figure class="thumb abs" style="left:97px"><div role="img" aria-label="Restaurant website screenshot with pasta dish" style="background:linear-gradient(#5b5a18 0 28%,#3a2a0a 28%,#8a4a0a 70%,#c98a1a)"></div></figure>
<figure class="thumb abs" style="left:381px"><div role="img" aria-label="Holiday gift shop website screenshot" style="background:linear-gradient(#f4f4f4 0 18%,#3a8ed0 18% 26%,#b0141c 26%,#d2283a)"></div></figure>
<figure class="thumb abs" style="left:663px"><div role="img" aria-label="Fitness gym website screenshot" style="background:linear-gradient(90deg,#1a1a1a 0 65%,#2a2a2a 65%),#111"></div></figure>

<footer class="footer abs"></footer>
<nav class="footer-links abs">Home<span>|</span>About Us<span>|</span>Portfolio<span>|</span>Contact Us</nav>
<p class="copyright abs">Copyright 2014 Brightmorrow Co.&nbsp; All right reserved.</p>
<div class="partner-badge abs" role="img" aria-label="Partner badge"><i></i></div>

</body>
</html>
```